Business card for Crestline Bathrooms

Please design a business card for our bathroom renovation business. You can use my existing logo, but if you have an idea to modernize it, I would like to see it. Please see attached files first. I would like to use the blue and the orange theme. I like the concept of using the shower head in the logo. Please find following a design (or two) that I have been trying to create with my limited resources. That design was for a sign, but I was going to adopt it and use it as a business card as well. I like the concept of the water splash but I don’t think it “flows” nicely together with the logo. Another thought is that maybe creating the logo out of water splash could work and have a dramatic effect (like the water text and the butterfly picture attached with similar background instead of white). If the above doesn’t work I would like to see a modern simplified design. One of the attached files named as the unwanted business card has all the details that I want included in the business card. Please note that it is two sided.
Updates

I am very thankful for the designs that I have received, but they are very similar and only a couple of attempts to do something with the water splash as per my original brief. Modernizing the logo and having it made out of out of water splash with the orange as color accent could work and have a dramatic effect (like the water text and the butterfly picture attached with similar background instead of white). Please do not use the butterfly itself! This is just an example that images can be created out of water splash.

Contact Information for Business Card

all the details are on the unwonted business card file included

Colors
3176b5

Requirements
Nice to have
• Copied from the brief:
• ... maybe creating the logo out of water splash could work and have a dramatic effect (like the water text and the butterfly picture attached with similar background instead of white). Please do not use the butterfly itself!
Should not have
• I am getting designs with a butterfly. The butterfly picture was an example of creating something from a water splash. The butterfly itself has no association with anything other than the concept of creating a logo out of water splash. Sorry, I thought I was clear in the brief.

```html
<!DOCTYPE html>
<html lang="en">
<head>
<meta charset="utf-8">
<title>Crestline Bathrooms – Business Card</title>
<link rel="stylesheet" href="https://fonts.googleapis.com/css2?family=Roboto:wght@400;500&family=Patrick+Hand&display=swap">
<style>
  :root {
    --canvas: #e3e3e3;
    --card-white: #ffffff;
    --navy: #0b3d6b;
    --name-blue: #1d4d7a;
    --icon-blue: #1f4f7c;
    --text-grey: #4a4a4a;
    --accent: #e8766a;
    --white: #ffffff;
    --splash-light: #e6edf3;
    --splash-mid: #9fb7cc;
    --splash-deep: #5f86a8;
  }
  * { box-sizing: border-box; margin: 0; padding: 0; }
  html, body { width: 1200px; height: 960px; overflow: hidden; }
  body {
    position: relative;
    background: var(--canvas);
    font-family: "Roboto", Arial, sans-serif;
  }
  .card { position: absolute; overflow: hidden; }

  /* Front */
  .card-front {
    left: 313px; top: 113px; width: 602px; height: 343px;
    background: var(--card-white);
  }
  .holder-name {
    position: absolute; left: 44px; top: 33px;
    font-family: "Patrick Hand", cursive;
    font-weight: 400;
    font-size: 30px; line-height: 36px; color: var(--name-blue); letter-spacing: 1px;
  }
  .postal-address {
    position: absolute; left: 45px; top: 81px;
    font-size: 15px; line-height: 18px; color: var(--text-grey);
  }
  .contact-list {
    position: absolute; left: 345px; top: 42px; list-style: none;
    font-size: 15px; line-height: 19px; color: var(--text-grey);
    white-space: nowrap;
  }
  .contact-list li { display: flex; align-items: center; gap: 8px; }
  .contact-list svg { width: 14px; height: 14px; fill: var(--icon-blue); flex: none; }
  .splash-photo {
    position: absolute; left: 0; right: 0; top: 150px; bottom: 0;
    background:
      radial-gradient(ellipse 45% 55% at 50% 75%, rgba(255,255,255,0.55), rgba(255,255,255,0) 70%),
      linear-gradient(180deg, var(--card-white) 0%, var(--splash-light) 20%, var(--splash-mid) 60%, var(--splash-deep) 100%);
  }

  /* Back */
  .card-back {
    left: 311px; top: 472px; width: 600px; height: 343px;
    background: var(--navy);
  }
  .brand-lockup {
    position: absolute; left: 52px; top: 122px;
    display: flex; align-items: center; gap: 14px; color: var(--white);
  }
  .brand-dot { width: 22px; height: 22px; border-radius: 50%; background: var(--accent); flex: none; }
  .brand-name { font-weight: 400; line-height: 1; }
  .brand-name .line-main { display: block; font-size: 44px; }
  .brand-name .line-sub { display: block; font-size: 21px; letter-spacing: 4px; margin-top: 8px; }
  .divider {
    position: absolute; left: 304px; top: 48px; width: 2px; height: 253px;
    background: var(--white);
  }
  .service-list {
    position: absolute; left: 340px; top: 45px; list-style: none;
    font-size: 15px; line-height: 19px; color: var(--white);
  }
  .service-list li { position: relative; padding-left: 15px; margin-bottom: 19px; }
  .service-list li::before {
    content: ""; position: absolute; left: 0; top: 6px;
    width: 6px; height: 6px; border-radius: 50%; background: var(--accent);
  }
  .member-badges {
    position: absolute; left: 340px; top: 266px;
    display: flex; align-items: center; gap: 16px;
  }
  .badge-square { width: 32px; height: 34px; border-radius: 6px; background: var(--white); }
  .badge-rule { width: 1px; height: 34px; background: var(--white); }
  .badge-wide { width: 118px; height: 22px; border-radius: 3px; background: var(--white); }
</style>
</head>
<body>

<section class="card card-front" aria-label="Card front">
  <h1 class="holder-name">Daniel Marovic</h1>
  <p class="postal-address">PO Box 41<br>Brindlewood 2620</p>
  <ul class="contact-list">
    <li><svg viewBox="0 0 24 24" aria-hidden="true"><path d="M6.6 10.8a15.1 15.1 0 0 0 6.6 6.6l2.2-2.2c.3-.3.7-.4 1-.2 1.1.4 2.3.6 3.6.6.6 0 1 .4 1 1V20c0 .6-.4 1-1 1A17 17 0 0 1 3 4c0-.6.4-1 1-1h3.5c.6 0 1 .4 1 1 0 1.3.2 2.5.6 3.6.1.3 0 .7-.2 1z"/></svg>0400 555 182</li>
    <li><svg viewBox="0 0 24 24" aria-hidden="true"><path d="M7 1h10a2 2 0 0 1 2 2v18a2 2 0 0 1-2 2H7a2 2 0 0 1-2-2V3a2 2 0 0 1 2-2zm0 4v13h10V5zm5 14.5a1.2 1.2 0 1 0 0 2.4 1.2 1.2 0 0 0 0-2.4z"/></svg>6200 5147</li>
    <li><svg viewBox="0 0 24 24" aria-hidden="true"><path d="M2 5h20v2l-10 6L2 7zm0 4.3 10 6 10-6V19H2z"/></svg>dan@crestlinebathrooms.com.au</li>
    <li><svg viewBox="0 0 24 24" aria-hidden="true"><path d="M12 2a10 10 0 1 0 0 20 10 10 0 0 0 0-20zm-1 17.9A8 8 0 0 1 4.2 10L9 14.8v1.1c0 1.1.9 2 2 2zm6.9-2.5A2 2 0 0 0 16 16h-1v-3a1 1 0 0 0-1-1H8v-2h2a1 1 0 0 0 1-1V7h2a2 2 0 0 0 2-2v-.4a8 8 0 0 1 2.9 12.8z"/></svg>crestlinebathrooms.com.au</li>
  </ul>
  <div class="splash-photo" role="img" aria-label="Photograph of a water droplet splash in soft blue tones"></div>
</section>

<section class="card card-back" aria-label="Card back">
  <div class="brand-lockup">
    <span class="brand-dot" aria-hidden="true"></span>
    <p class="brand-name"><span class="line-main">Crestline</span><span class="line-sub">Bathrooms</span></p>
  </div>
  <div class="divider" aria-hidden="true"></div>
  <ul class="service-list">
    <li>Complete Bathroom<br>Renovations &amp; Remodelling</li>
    <li>Highly Skilled &amp;<br>Qualified Tradespeople</li>
    <li>Professional Service From<br>Concept To Completion</li>
    <li>All Work Guaranteed</li>
  </ul>
  <div class="member-badges" aria-label="Industry association memberships">
    <span class="badge-square"></span>
    <span class="badge-rule"></span>
    <span class="badge-wide"></span>
  </div>
</section>

</body>
</html>
```